Re-Design WP Site BrightPebbles.info

Site Re-design. Also Need a Button for contact on main page. Need Great Looking products re designed. Also bonus if you can install a site SEO checker on the site.

BrightPebbles.info

```html
<!DOCTYPE html>
<html lang="en">
<head>
<meta charset="utf-8">
<title>Bright Pebbles — Home</title>
<link rel="stylesheet" href="https://fonts.googleapis.com/css2?family=Poppins:wght@400;500;600;700&display=swap">
<style>
  :root {
    --page-bg: #ffffff;
    --ink: #1f2433;
    --nav-ink: #4a4f5c;
    --accent: #1a73e8;
    --outline: #1e88e5;
    --hero-deep: #08247a;
    --hero-mid: #0c3396;
    --icon-ink: #3b5ba9;
    --cap-start: #1aa3f0;
    --cap-end: #1f4fd8;
    --white: #ffffff;
  }
  * { box-sizing: border-box; margin: 0; padding: 0; }
  html, body { width: 1200px; height: 813px; overflow: hidden; background: var(--page-bg); }
  body { position: relative; font-family: "Poppins", sans-serif; color: var(--ink); }

  .site-header { position: absolute; left: 0; top: 0; width: 1200px; height: 70px; }
  .brand { position: absolute; left: 82px; top: 22px; display: flex; align-items: center; gap: 9px;
           font-weight: 600; font-size: 24px; color: var(--ink); letter-spacing: -0.2px; }
  .brand-dot { width: 18px; height: 18px; border-radius: 50%; background: var(--accent); }
  .main-nav { position: absolute; top: 26px; left: 0; width: 1200px; font-size: 13.5px; color: var(--nav-ink); }
  .main-nav a { position: absolute; color: inherit; text-decoration: none; white-space: nowrap; }
  .main-nav a.is-current { color: var(--accent); font-weight: 500; }
  .main-nav a.is-current::after { content: ""; position: absolute; left: 0; right: 0; bottom: -7px;
           height: 2.5px; border-radius: 2px; background: var(--accent); }

  .hero-frame { position: absolute; left: 0; top: 0; }
  .hero-copy { position: absolute; left: 189px; top: 155px; width: 420px; color: var(--white); }
  .hero-title { font-weight: 700; font-size: 34px; line-height: 1.1; white-space: nowrap; }
  .hero-subtitle { margin-top: 20px; font-weight: 600; font-size: 22px; }
  .hero-text { margin-top: 24px; font-size: 16px; line-height: 30px; font-weight: 400; }
  .hero-cta { position: absolute; left: 189px; top: 399px; width: 208px; height: 50px; border-radius: 25px;
              background: var(--white); color: var(--accent); font-weight: 600; font-size: 15px;
              display: flex; align-items: center; justify-content: center; text-decoration: none; }
  .hero-media { position: absolute; left: 661px; top: 206px; width: 351px; height: 198px; border-radius: 10px;
                background: linear-gradient(135deg, #3a2a3a 0%, #1d2430 45%, #243a2a 75%, #5a6a58 100%); }
  .play-button { position: absolute; left: 157px; top: 82px; width: 36px; height: 36px; border-radius: 50%;
                 background: var(--white); display: flex; align-items: center; justify-content: center; }

  .services { position: absolute; left: 0; top: 541px; width: 1200px; }
  .service { position: absolute; width: 200px; margin-left: -100px; text-align: center; }
  .service-badge { display: block; margin: 0 auto; filter: drop-shadow(0 6px 10px rgba(40, 80, 180, 0.12)); }
  .service-label { margin-top: 30px; font-size: 16.5px; line-height: 25px; color: var(--ink); }
</style>
</head>
<body>

<header class="site-header">
  <div class="brand"><span class="brand-dot"></span>Bright Pebbles</div>
  <nav class="main-nav">
    <a class="is-current" href="#" style="left:570px">Home</a>
    <a href="#" style="left:660px">Shop</a>
    <a href="#" style="left:744px">Solutions</a>
    <a href="#" style="left:855px">Blog</a>
    <a href="#" style="left:935px">Auctions</a>
    <a href="#" style="left:1044px">Contact Us</a>
  </nav>
</header>

<svg class="hero-frame" width="1200" height="500" viewBox="0 0 1200 500" aria-hidden="true">
  <defs>
    <linearGradient id="heroFill" x1="0" y1="0" x2="1" y2="1">
      <stop offset="0" stop-color="var(--hero-mid)"/>
      <stop offset="1" stop-color="var(--hero-deep)"/>
    </linearGradient>
  </defs>
  <polyline fill="none" stroke="var(--outline)" stroke-width="1.6"
    points="82,465 69,465 69,163 165,113 206,113"/>
  <polyline fill="none" stroke="var(--outline)" stroke-width="1.6"
    points="389,114 422,94 809,94 867,78 1131,78 1131,392 1118,404"/>
  <polygon fill="url(#heroFill)"
    points="82,167 206,106 295,106 316,114 389,114 422,106 809,106 867,90 1118,90 1118,404 1046,479 703,479 683,490 516,490 495,479 82,479"/>
</svg>

<section class="hero">
  <div class="hero-copy">
    <h1 class="hero-title">Welcome to Bright Pebbles</h1>
    <h2 class="hero-subtitle">We Are Digital Innovators</h2>
    <p class="hero-text">We’re a studio of creators inventing unique and effective IT applications providing solutions that solve real world problems.</p>
  </div>
  <a class="hero-cta" href="#">Explore our Offerings</a>
  <div class="hero-media" role="img" aria-label="Video still of a team working at monitors in a control room">
    <span class="play-button">
      <svg width="12" height="12" viewBox="0 0 12 12" aria-hidden="true"><path d="M3 1.5 L10.5 6 L3 10.5 Z" fill="var(--accent)"/></svg>
    </span>
  </div>
</section>

<svg width="0" height="0" style="position:absolute" aria-hidden="true">
  <defs>
    <linearGradient id="capFill" x1="0" y1="0" x2="1" y2="0">
      <stop offset="0" stop-color="var(--cap-start)"/>
      <stop offset="1" stop-color="var(--cap-end)"/>
    </linearGradient>
    <symbol id="badge" viewBox="0 0 138 166">
      <polygon points="69,0 138,41 138,125 69,166 0,125 0,41" fill="url(#capFill)"/>
      <polygon points="69,14 138,55 138,125 69,166 0,125 0,55" fill="#ffffff"/>
    </symbol>
  </defs>
</svg>

<section class="services">
  <div class="service" style="left:251px">
    <svg class="service-badge" width="138" height="166" viewBox="0 0 138 166" aria-hidden="true">
      <use href="#badge"/>
      <g fill="none" stroke="var(--icon-ink)" stroke-width="4" stroke-linecap="round">
        <circle cx="66" cy="92" r="26"/>
        <path d="M42 84 Q66 98 90 84 M48 108 Q64 92 86 104 M66 66 Q56 92 66 118"/>
        <path d="M76 76 L94 94" stroke-width="6"/>
        <circle cx="79" cy="73" r="6"/>
      </g>
    </svg>
    <p class="service-label">Full Service Offsite<br>and Onsite</p>
  </div>

  <div class="service" style="left:473px">
    <svg class="service-badge" width="138" height="166" viewBox="0 0 138 166" aria-hidden="true">
      <use href="#badge"/>
      <g fill="none" stroke="var(--icon-ink)" stroke-width="4" stroke-linecap="round" stroke-linejoin="round">
        <rect x="38" y="78" width="18" height="34" rx="3"/>
        <path d="M56 84 L98 84 L98 104 M66 104 L104 104 L104 110 L62 110"/>
      </g>
      <circle cx="89" cy="68" r="11" fill="var(--icon-ink)"/>
      <circle cx="89" cy="65" r="4" fill="#ffffff"/>
    </svg>
    <p class="service-label">Create Public and a<br>Cohesive Profile of</p>
  </div>

  <div class="service" style="left:712px">
    <svg class="service-badge" width="138" height="166" viewBox="0 0 138 166" aria-hidden="true">
      <use href="#badge"/>
      <g fill="none" stroke="var(--icon-ink)" stroke-width="4" stroke-linecap="round" stroke-linejoin="round">
        <path d="M46 76 L52 62 L96 62 L102 76 Q98 84 90 80 Q82 86 74 80 Q66 86 58 80 Q50 84 46 76 Z"/>
        <path d="M52 84 L52 90 M96 82 L96 110 L70 110"/>
        <path d="M38 108 L48 98 Q54 94 58 100 M50 112 Q44 118 40 112 M56 104 L46 114"/>
      </g>
    </svg>
    <p class="service-label">Get Links from High<br>Authority Sites to</p>
  </div>

  <div class="service" style="left:950px">
    <svg class="service-badge" width="138" height="166" viewBox="0 0 138 166" aria-hidden="true">
      <use href="#badge"/>
      <g fill="none" stroke="var(--icon-ink)" stroke-width="4" stroke-linecap="round" stroke-linejoin="round">
        <path d="M46 76 L52 62 L96 62 L102 76 Q98 84 90 80 Q82 86 74 80 Q66 86 58 80 Q50 84 46 76 Z"/>
        <path d="M52 84 L52 92 M96 82 L96 110 L66 110"/>
        <path d="M42 100 L58 116" stroke-width="6"/>
        <circle cx="40" cy="98" r="5"/>
      </g>
    </svg>
    <p class="service-label">Optimize Searchly<br>Business Profile</p>
  </div>
</section>

</body>
</html>
```